Realistisches bis futuristisch abstraktes CD-Cover für progressive Metal/Djent Band
Zielgruppe
Wir sind eine progressive Metal/Djent Band, unsere Zielgruppe sind liebhaber moderner Metalmusik im alter von 14-45.
Aufgabenstellung
Bitte keine Zeichnungen. Das Cover soll realistisch bis futuristisch abstrakt sein.
Zu berücksichtigen ist auch die Message des Albums: Das Album wird Fulcrum//Vertigo//Umbra heißen, es ist in diese drei Teile aufgeteilt und verfolgt eine durchgehende Geschichte wobei das Ende offen gelassen wird und die Möglichkeit besteht dass der Protagonist/die Protagonistin wieder in alte Muster zurück fällt und alles von neuem beginnt (ein Teufelskreis sozusagen.
In der Geschichte geht es konkret darum dass der Protagonist/die Protagonistin von Angst und Depression überwältigt wird und die Kontrolle über sich selbst verliert (Fulcrum). Im zweiten Teil (Vertigo) geht der Protagonist/die Protagonistin dann konkret auf den unverarbeiteten Emotionalen Ballast der Vergangenheit ein und findet den Ursprung der Angst/Depression heraus. Im 3en Teil (Umbra) findet der Protagonist/die Portagonistin dann wieder zu sich selbst und legt alles daran den Feind (also die Angst/Depression) zu bekämpfen. Der letzte Song, Hollowmerest, welcher alleine steht und keinem Teil direkt zugehörig ist zeigt dann den Showdown zwischen Vernunft und Angst/Depression und lässt offen ob der Protagonist/die Protagonistin wirklich den Schritt schafft um die Angst/Depression hinter sich zu lassen (letzte Zeile der Lyrics: Can I transcend?)
Das Album ist ein Konzeptalbum und ist lyrisch und musikalisch durchgängig, daher soll das Cover auch gut dazu passen.
Viel Spaß beim designen, ich bin gespannt auf die visuellen Umsetzungen meiner Ideen.
PS: Die upgeloadeten Bilder sollen im Booklet sein und es sollte stimmig mit dem Cover sein. Weiters kommen auch noch die Lyrics ins Booklet.
copiright der Bilder: Ferdinand Waltraker

```html
<!DOCTYPE html>
<html lang="de">
<head>
<meta charset="utf-8">
<title>Fulcrum//Vertigo//Umbra – Cover</title>
<link rel="stylesheet" href="https://fonts.googleapis.com/css2?family=Jost:wght@600&display=swap">
<style>
  :root {
    --bg-core: #1c2734;
    --bg-edge: #0b1016;
    --ink: #dcdcdc;
    --stripe: #d6d6d6;
  }
  html, body {
    margin: 0;
    padding: 0;
    overflow: hidden;
    background: var(--bg-edge);
  }
  .cover {
    position: relative;
    width: 1200px;
    height: 1190px;
    overflow: hidden;
  }
  .cover-art {
    display: block;
    width: 1200px;
    height: 1190px;
  }
  .stripe {
    fill: none;
    stroke: var(--stripe);
    stroke-width: 2.6;
    stroke-linejoin: miter;
  }
  .part-title {
    fill: var(--ink);
    font-family: "Jost", "Futura", sans-serif;
    font-weight: 600;
    font-size: 136px;
    letter-spacing: 0;
  }
</style>
</head>
<body>
  <main class="cover">
    <svg class="cover-art" viewBox="0 0 1430 1418" preserveAspectRatio="none" xmlns="http://www.w3.org/2000/svg">
      <defs>
        <radialGradient id="surface" cx="45%" cy="40%" r="75%">
          <stop offset="0" stop-color="var(--bg-core)"/>
          <stop offset="1" stop-color="var(--bg-edge)"/>
        </radialGradient>
      </defs>

      <rect class="surface" role="img" aria-label="Dunkle, raue Beton- bzw. Schiefertextur in Blauschwarz" x="0" y="0" width="1430" height="1418" fill="url(#surface)"/>

      <g class="divider divider-left">
        <polygon class="stripe" points="417,490 433,490 140,1418 124,1418"/>
        <polygon class="stripe" points="504,490 522,490 476,620 458,620"/>
      </g>

      <g class="divider divider-right">
        <polygon class="stripe" points="1270,0 1287,0 993,935 976,935"/>
        <polygon class="stripe" points="927,802 945,802 898,935 880,935"/>
      </g>

      <text class="part-title part-one" x="232" y="438">FULCRUM</text>
      <text class="part-title part-two" x="420" y="758">VERTIGO</text>
      <text class="part-title part-three" x="722" y="1078">UMBRA</text>
    </svg>
  </main>
</body>
</html>
```